The 50 Year History of the Tallowmere Whippet Coursing Society

The Tallowmere Whippet Coursing Society has been established for 50 years last month. We are putting together a chronological history book with interesting stories about events over the past 50 years.
Book title: Swift Across Decades: 50 Years of the Tallowmere Whippet Coursing Society
Front Cover: We are looking for a simple but striking design. It must have at least one racing greyhound (image from Australia). I can supply images of greyhounds if required. It must have our logo.
Back Cover: can be minimal with club details
Book Size: A4

```html
<!DOCTYPE html>
<html lang="en">
<head>
<meta charset="utf-8">
<title>Swift Across Decades – Book Cover</title>
<link rel="stylesheet" href="https://fonts.googleapis.com/css2?family=Cinzel:wght@700&family=Poppins:wght@400&display=swap">
<style>
  :root {
    --backdrop: #e6e6e6;
    --track-tan: #b9996b;
    --track-light: #c9ad80;
    --track-far: #8f8a62;
    --band-tan: #b09560;
    --title-rust: #7b3009;
    --ink: #111111;
    --footer-white: #ffffff;
    --mark-green: #2f8a2a;
  }
  html, body {
    margin: 0;
    width: 1200px;
    height: 800px;
    overflow: hidden;
    background: var(--backdrop);
  }
  .canvas {
    position: relative;
    width: 1200px;
    height: 800px;
  }
  .book-cover {
    position: absolute;
    left: 345px;
    top: 40px;
    width: 509px;
    height: 720px;
    display: block;
  }
  .cover-title {
    font-family: "Cinzel", "Times New Roman", serif;
    font-weight: 700;
    fill: var(--title-rust);
  }
  .cover-subtitle {
    font-family: "Poppins", Arial, sans-serif;
    font-weight: 400;
    font-size: 20px;
    fill: var(--ink);
  }
  .club-name {
    font-family: "Poppins", Arial, sans-serif;
    font-weight: 400;
    font-size: 17px;
    fill: var(--ink);
  }
</style>
</head>
<body>
<main class="canvas">
  <svg class="book-cover" viewBox="0 0 509 720" xmlns="http://www.w3.org/2000/svg">
    <defs>
      <linearGradient id="trackGradient" x1="0" y1="0" x2="0" y2="1">
        <stop offset="0" stop-color="var(--track-far)"/>
        <stop offset="0.12" stop-color="var(--track-light)"/>
        <stop offset="1" stop-color="var(--track-tan)"/>
      </linearGradient>
    </defs>

    <rect class="cover-photo" x="0" y="0" width="509" height="335" fill="url(#trackGradient)"
          role="img" aria-label="Photograph of a whippet sprinting along a sandy coursing track beside a white-railed fence"/>

    <rect class="cover-band" x="0" y="335" width="509" height="307" fill="var(--band-tan)"/>

    <text class="cover-title" x="31" y="333" font-size="92" textLength="432" lengthAdjust="spacingAndGlyphs">SWIFT</text>
    <text class="cover-title" x="38" y="402" font-size="70" textLength="421" lengthAdjust="spacingAndGlyphs">ACROSS</text>
    <text class="cover-title" x="25" y="534" font-size="150" textLength="444" lengthAdjust="spacingAndGlyphs">DECADES</text>

    <text class="cover-subtitle" x="254.5" y="566" text-anchor="middle">50 YEARS OF THE TALLOWMERE WHIPPET</text>
    <text class="cover-subtitle" x="254.5" y="598" text-anchor="middle">COURSING SOCIETY</text>

    <rect class="cover-footer" x="0" y="642" width="509" height="78" fill="var(--footer-white)"/>
    <circle class="club-dot" cx="90" cy="681" r="9" fill="var(--mark-green)"/>
    <text class="club-name" x="110" y="687">Tallowmere Whippet Coursing Society</text>
  </svg>
</main>
</body>
</html>
```